Unique business card design

Boutique coastal hotel suites - in need of clever stand out business card I have uploaded the logo that I had created through quill forge I want something that is clever and stands out from everyone else - 418 Brantwell Avenue kelwick Alaska 99571 phone or text 907 -581-6142 www.primemarrowbysuites.com

Target Market(s)

Men and woman

Industry/Entity Type

Boutique coastal hotel

Contact Information for Business Card

Marrowby Suites kelwick Alaska marrowby_suites@mailnest.net

Requirements
Must have
• Classy - clever -bold 907-581-6142 call or text

```html
<!DOCTYPE html>
<html lang="en">
<head>
<meta charset="utf-8">
<title>Marrowby Suites – Business Card</title>
<link href="https://fonts.googleapis.com/css2?family=Source+Sans+3:wght@400;600&display=swap" rel="stylesheet">
<style>
  :root {
    --backdrop: #fdf5e4;
    --card: #f1eee8;
    --navy: #2b516d;
    --red: #d42429;
    --yellow: #f6d53f;
    --ink: #1d1d1d;
  }
  * { box-sizing: border-box; margin: 0; padding: 0; }
  html, body { width: 1200px; height: 507px; overflow: hidden; }
  body {
    background: var(--backdrop);
    position: relative;
    font-family: "Source Sans 3", "Myriad Pro", sans-serif;
    color: var(--ink);
  }
  .card {
    position: absolute;
    top: 90px;
    width: 505px;
    height: 288px;
    background: var(--card);
  }
  .card--front { left: 71px; }
  .card--back { left: 616px; }

  .band {
    position: absolute;
    left: 0; right: 0;
    height: 13px;
    display: flex;
  }
  .band--top { top: 0; }
  .band--bottom { bottom: 0; }
  .band span { flex: 1; }
  .navy { background: var(--navy); }
  .red { background: var(--red); }
  .yellow { background: var(--yellow); }

  .brand {
    position: absolute;
    display: flex;
    align-items: center;
    color: var(--navy);
    font-weight: 600;
    letter-spacing: 0.14em;
    text-transform: uppercase;
    white-space: nowrap;
  }
  .brand__mark { background: var(--red); flex: none; }
  .card--front .brand {
    left: 0; right: 0; top: 128px;
    justify-content: center;
    font-size: 26px;
    gap: 12px;
  }
  .card--front .brand__mark { width: 16px; height: 16px; }
  .card--back .brand {
    left: 21px; top: 40px;
    font-size: 16px;
    gap: 8px;
  }
  .card--back .brand__mark { width: 10px; height: 10px; }

  .contact {
    position: absolute;
    left: 275px;
    top: 137px;
    list-style: none;
    font-size: 13px;
    line-height: 16px;
  }
  .contact li {
    display: flex;
    align-items: center;
    gap: 9px;
    margin-bottom: 12px;
  }
  .contact li.contact__address { margin-bottom: 10px; }
  .contact svg { width: 14px; height: 14px; flex: none; fill: var(--navy); }
</style>
</head>
<body>
  <section class="card card--front">
    <div class="band band--top"><span class="navy"></span><span class="red"></span><span class="yellow"></span></div>
    <div class="brand"><span class="brand__mark"></span>Marrowby Suites</div>
    <div class="band band--bottom"><span class="yellow"></span><span class="red"></span><span class="navy"></span></div>
  </section>

  <section class="card card--back">
    <div class="band band--top"><span class="navy"></span><span class="red"></span><span class="yellow"></span></div>
    <div class="brand"><span class="brand__mark"></span>Marrowby Suites</div>

    <ul class="contact">
      <li class="contact__address">
        <svg viewBox="0 0 24 24" aria-hidden="true"><path d="M12 2a7 7 0 0 0-7 7c0 5 7 13 7 13s7-8 7-13a7 7 0 0 0-7-7zm0 9.5a2.5 2.5 0 1 1 0-5 2.5 2.5 0 0 1 0 5z"/></svg>
        <span>418 Brantwell Avenue,<br>kelwick Alaska</span>
      </li>
      <li>
        <svg viewBox="0 0 24 24" aria-hidden="true"><path d="M6.6 10.8a15.1 15.1 0 0 0 6.6 6.6l2.2-2.2c.3-.3.7-.4 1-.2 1.1.4 2.3.6 3.6.6.6 0 1 .4 1 1V20c0 .6-.4 1-1 1A17 17 0 0 1 3 4c0-.6.4-1 1-1h3.5c.6 0 1 .4 1 1 0 1.3.2 2.5.6 3.6.1.3 0 .7-.2 1z"/></svg>
        <span>907 -581-6142</span>
      </li>
      <li>
        <svg viewBox="0 0 24 24" aria-hidden="true"><path d="M3 6a2 2 0 0 1 2-2h14a2 2 0 0 1 2 2v.4l-9 5.4-9-5.4z"/><path d="M3 8.7l9 5.4 9-5.4V18a2 2 0 0 1-2 2H5a2 2 0 0 1-2-2z"/></svg>
        <span>marrowby_suites@mailnest.net</span>
      </li>
      <li>
        <svg viewBox="0 0 24 24" aria-hidden="true"><path d="M12 2a10 10 0 1 0 0 20 10 10 0 0 0 0-20zm0 2c1 0 2.2 1.8 2.8 5H9.2C9.8 5.8 11 4 12 4zM4.3 10h3.8a18 18 0 0 0 0 4H4.3a8 8 0 0 1 0-4zm1 6h3c.3 1.6.8 2.9 1.4 3.8A8 8 0 0 1 5.3 16zm3-8h-3a8 8 0 0 1 4.4-3.8C9.1 5.1 8.6 6.4 8.3 8zM12 20c-1 0-2.2-1.8-2.8-4h5.6c-.6 2.2-1.8 4-2.8 4zm3-6H9a16 16 0 0 1 0-4h6a16 16 0 0 1 0 4zm.7-9.8A8 8 0 0 1 18.7 8h-3c-.3-1.6-.8-2.9-1.4-3.8zM15.9 10h3.8a8 8 0 0 1 0 4h-3.8a18 18 0 0 0 0-4zm-2.2 9.8c.6-.9 1.1-2.2 1.4-3.8h3a8 8 0 0 1-4.4 3.8z"/></svg>
        <span>www.primemarrowbysuites.com</span>
      </li>
    </ul>

    <div class="band band--bottom"><span class="yellow"></span><span class="red"></span><span class="navy"></span></div>
  </section>
</body>
</html>
```